New Business Card Design for Manufacturing

We are an engineering/manufacturing company that offers Advanced machining/assembly/engineering services, as well as innovative products for the heavy duty engine cooling markets.

We are looking to get a new business card designed that is clean and modern looking, but still fits the wide range of technical/skilled work we do.

- We hope to use this design as the base for other design work in new Presentations, web, and print work.

Industry/Entity Type

Engineering

Contact Information for Business Card

Our preferred color of blue is (RGB) 22/71/159 but can vary slightly from that color. Our content will be our Logo and full company name (Corvath Tooling Works, Inc.), company address, name, job title, phone number with extension, cell number, fax number, website, and email address on the cards.
We'd like the full company name next to the logo, but we are open to other interpretations of that layout.
Preferably, we would like the back side to be clean with just our logo, and the front to contain all of the contact information.

Colors
2f74b4
0355a3
85abd2

Requirements
Must have
• - Logo, company name, needed content - We are open to interpretation beyond that.
• - Standard size business card.
• - Horizontal orientation.
• - Enough space for lengthy names / job titles (for example, a job title could read "Directory of Human Resources" or "V.P. of Governmental Affairs"). We need this to look clean, whether the title be short (CEO) or long (as described above).

```html
<!DOCTYPE html>
<html lang="en">
<head>
<meta charset="utf-8">
<title>Corvath Tooling Works – Business Card</title>
<link rel="stylesheet" href="https://fonts.googleapis.com/css2?family=Open+Sans:wght@400;600;700;800&display=swap">
<style>
  :root{
    --bg:#e9ebee;
    --blue-deep:#0d3a82;
    --blue:#16479f;
    --blue-mid:#2f74b4;
    --blue-brand:#0355a3;
    --blue-light:#85abd2;
    --blue-bright:#4a9ad8;
    --white:#ffffff;
    --paper:#f6f7f8;
  }
  *{margin:0;padding:0;box-sizing:border-box}
  html,body{width:1200px;height:1200px;overflow:hidden;background:var(--bg);font-family:"Open Sans",Arial,sans-serif}
  .canvas{position:relative;width:1200px;height:1200px}
  .card{position:absolute;left:150px;width:900px;height:514px;border-radius:6px;overflow:hidden;box-shadow:0 12px 30px rgba(0,0,0,.18)}
  .card--front{top:60px;background:linear-gradient(160deg,var(--blue) 0%,var(--blue-deep) 55%,#0b3172 100%);color:var(--white)}
  .card--back{top:626px;background:var(--paper)}

  .front__wordmark{position:absolute;left:60px;top:40px;font-weight:800;font-size:64px;letter-spacing:-1px;line-height:1;color:var(--white)}
  .front__company{position:absolute;left:520px;top:92px;font-weight:800;font-size:30px;line-height:30px;letter-spacing:1px;text-transform:uppercase;color:var(--white)}
  .front__company small{font-size:13px;letter-spacing:0;margin-left:4px}

  .front__name{position:absolute;left:60px;top:140px;font-weight:600;font-size:40px;line-height:1.1}
  .front__title{position:absolute;left:62px;top:196px;font-weight:600;font-size:17px}
  .front__rule{position:absolute;left:40px;right:0;top:236px;height:4px;background:var(--white)}
  .front__tab{position:absolute;left:0;width:12px;height:70px;background:#dfe6ef;border-radius:0 6px 6px 0}
  .front__tab--top{top:150px}
  .front__tab--bottom{top:262px}

  .contact{position:absolute;left:60px;top:256px;list-style:none;font-size:14px;line-height:20px;color:#e6eefb}
  .contact li{display:flex;align-items:flex-start;gap:10px;margin-bottom:4px}
  .contact svg{flex:0 0 14px;margin-top:3px}

  .front__band{position:absolute;left:0;right:0;bottom:0;height:96px;background:linear-gradient(90deg,var(--blue-bright) 0%,var(--blue-mid) 60%,var(--blue-brand) 100%)}
  .front__site{position:absolute;left:60px;bottom:30px;font-weight:700;font-size:26px;color:var(--white)}
  .front__watermark{position:absolute;right:-20px;bottom:80px;font-weight:800;font-size:150px;line-height:1;color:rgba(133,171,210,.12);letter-spacing:-3px}

  .back__wordmark{position:absolute;left:0;right:0;top:50%;transform:translateY(-50%);text-align:center;font-weight:800;font-size:96px;letter-spacing:-2px;color:var(--blue-brand)}
</style>
</head>
<body>
<main class="canvas">

  <section class="card card--front" aria-label="Business card front">
    <div class="front__watermark" aria-hidden="true">Corvath</div>
    <div class="front__wordmark">Corvath</div>
    <div class="front__company">Corvath<br>Tooling<br>Works<small>INC</small></div>

    <span class="front__tab front__tab--top"></span>
    <span class="front__tab front__tab--bottom"></span>

    <h1 class="front__name">Full Name</h1>
    <p class="front__title">Office</p>
    <div class="front__rule"></div>

    <ul class="contact">
      <li>
        <svg width="14" height="14" viewBox="0 0 24 24" fill="#fff"><path d="M6.6 10.8a15 15 0 0 0 6.6 6.6l2.2-2.2c.3-.3.7-.4 1-.2 1.1.4 2.3.6 3.6.6.6 0 1 .4 1 1V20c0 .6-.4 1-1 1A17 17 0 0 1 3 4c0-.6.4-1 1-1h3.5c.6 0 1 .4 1 1 0 1.3.2 2.5.6 3.6.1.3 0 .7-.2 1z"/></svg>
        <span>Tel. +1 555 018 2740 ext. 12<br>Fax. +1 555 018 2741</span>
      </li>
      <li>
        <svg width="14" height="14" viewBox="0 0 24 24" fill="none" stroke="#fff" stroke-width="2"><rect x="3" y="5" width="18" height="14" rx="1"/><path d="M3 6l9 7 9-7"/></svg>
        <span>office@corvath.com</span>
      </li>
      <li>
        <svg width="14" height="14" viewBox="0 0 24 24" fill="#fff"><path d="M12 2a7 7 0 0 0-7 7c0 5 7 13 7 13s7-8 7-13a7 7 0 0 0-7-7zm0 9.5A2.5 2.5 0 1 1 12 6.5a2.5 2.5 0 0 1 0 5z"/></svg>
        <span>12 Forge Lane, Unit 4<br>Millbrook, OH 44001</span>
      </li>
    </ul>

    <div class="front__band"></div>
    <p class="front__site">www.corvathtooling.com</p>
  </section>

  <section class="card card--back" aria-label="Business card back">
    <div class="back__wordmark">Corvath</div>
  </section>

</main>
</body>
</html>
```